Products We Offer Line Card

I want to create a multi page document that outlines all of the Products that my dealership sells. We have many brands and we would like to be able to carry this document to customers and present all of our products. Attached you will find the product logo and a picture of the product.

Target Market(s)

Contractors

Colors
EB3D1F
EC4F4E
F09395
F8D3D4
FCEDEE

Requirements
Must have
• There will be multiple products per page. I am thinking 4 products per page and approx. 10 pages total. I would like for my logo and contact info to be on the cover page of the catalog. I will attach the logo file now. Address: 4362 Marrowfield Rd. Easley, SC 29640 Phone: (864) 555-0147 www.brovanmachinery.example

```html
<!DOCTYPE html>
<html lang="en">
<head>
<meta charset="utf-8">
<title>Brovan Machinery – Product Catalog 2024</title>
<link rel="stylesheet" href="https://fonts.googleapis.com/css2?family=Poppins:wght@200;500;700;800&display=swap">
<style>
  :root {
    --brand-red: #ed1f2b;
    --steel-grey: #7f8596;
    --ink: #111111;
    --paper: #ffffff;
  }
  html, body {
    margin: 0;
    padding: 0;
    overflow: hidden;
    background: var(--paper);
  }
  .catalog-cover {
    position: relative;
    width: 848px;
    height: 1200px;
    overflow: hidden;
    background: var(--paper);
    font-family: "Poppins", sans-serif;
  }
  .cover-art {
    position: absolute;
    inset: 0;
    width: 848px;
    height: 1200px;
  }
  .grey-fill { fill: var(--steel-grey); }
  .red-fill { fill: var(--brand-red); }
  .ink-fill { fill: var(--ink); }
  .brand-name {
    font-family: "Poppins", sans-serif;
    font-weight: 800;
    fill: var(--ink);
  }
  .title-product {
    font-family: "Poppins", sans-serif;
    font-weight: 700;
    fill: var(--steel-grey);
  }
  .title-catalog {
    font-family: "Poppins", sans-serif;
    font-weight: 200;
    fill: var(--ink);
  }
  .title-year {
    font-family: "Poppins", sans-serif;
    font-weight: 700;
    fill: var(--brand-red);
  }
  .site-address {
    font-family: "Poppins", sans-serif;
    font-weight: 700;
    fill: var(--paper);
  }
  .contact-line {
    font-family: "Poppins", sans-serif;
    font-weight: 500;
    fill: var(--paper);
  }
</style>
</head>
<body>
<main class="catalog-cover">
  <svg class="cover-art" viewBox="0 0 1622 2296" preserveAspectRatio="none" xmlns="http://www.w3.org/2000/svg">
    <defs>
      <linearGradient id="site-photo-tone" x1="0" y1="0" x2="0" y2="1">
        <stop offset="0" stop-color="#d9d0b2"/>
        <stop offset="0.45" stop-color="#b7b1a4"/>
        <stop offset="1" stop-color="#5f5a52"/>
      </linearGradient>
    </defs>

    <!-- brand mark -->
    <rect x="98" y="86" width="120" height="120" class="red-fill"/>
    <text class="brand-name" x="250" y="196" font-size="136" textLength="640" lengthAdjust="spacingAndGlyphs">BROVAN</text>
    <text class="brand-name" x="100" y="252" font-size="50" textLength="785" lengthAdjust="spacing">MACHINERY</text>

    <!-- grey backdrop -->
    <polygon class="grey-fill" points="0,258 665,462 255,795 470,1012 0,1680"/>

    <!-- red diagonal stripes -->
    <polygon class="red-fill" points="0,620 0,706 625,1332 712,1332"/>
    <polygon class="red-fill" points="0,765 0,872 318,1186 424,1186"/>

    <!-- photo frame -->
    <polygon class="ink-fill" points="1245,0 1622,0 1622,1470 1272,1836 250,798"/>
    <polygon role="img" aria-label="Construction site with scaffolding, a tower crane and stacked formwork panels"
             fill="url(#site-photo-tone)" points="1245,0 1622,0 1622,1460 1272,1820 266,795"/>

    <!-- lower right bands -->
    <polygon class="grey-fill" points="1188,1912 1622,1478 1622,1568 1188,2002"/>
    <polygon class="grey-fill" points="1258,1998 1622,1634 1622,1748 1258,2106"/>
    <polygon class="red-fill" points="1622,1760 1622,2296 1230,2296 1100,2170 1280,2010"/>

    <!-- footer band -->
    <path class="ink-fill" d="M0,2296 L0,2265 C60,2200 140,2170 240,2170 L1105,2170 L1240,2296 Z"/>

    <!-- titles -->
    <text class="title-product" x="176" y="1722" font-size="176" textLength="604" lengthAdjust="spacingAndGlyphs">Product</text>
    <text class="title-catalog" x="178" y="1846" font-size="150" textLength="538" lengthAdjust="spacingAndGlyphs">Catalog</text>
    <text class="title-year" x="562" y="2068" font-size="224" textLength="568" lengthAdjust="spacingAndGlyphs">2024</text>

    <!-- contact -->
    <text class="site-address" x="660" y="2228" font-size="46" text-anchor="middle" textLength="720" lengthAdjust="spacingAndGlyphs">www.brovanmachinery.example</text>
    <text class="contact-line" x="660" y="2274" font-size="27" text-anchor="middle" textLength="760" lengthAdjust="spacingAndGlyphs">4362 Marrowfield Rd. Easley, SC 29640  |  (864) 555-0147</text>
  </svg>
</main>
</body>
</html>
```